Kveldbrá - Start-up company selling electricity

Hello let me tell you about Kveldbrá.

Kveldbrá is start-up company selling electricity in Iceland. The operations of the company consist of making power usage forecasts for our customers, purchasing the electricity wholesale from the energy producers, and selling the electricity to the consumer. We are focused on tech by using optimization and machine learning to minimize electricity prices to our customers. Our marketing strategy is to portray a tech company mindset and to show dedication to driving down the electricity price on the market.

We need your help to make our website pop. Possible concepts to work with are as follows:

- Iceland the land of ice and fire
- Green energy
- Innovation
- Tech and data science

Link to our website: https://prufa.kveldbra.is/
We are open to ideas.
Thank you!

Target Market(s)

Electricity consumers both homes and companies.

Number of Pages Required

1 page

Font styles to use
Serif
Sans Serif

```html
<!DOCTYPE html>
<html lang="is">
<head>
<meta charset="utf-8">
<title>Kveldbrá - Same electricity, just cheaper</title>
<link rel="stylesheet" href="https://fonts.googleapis.com/css2?family=Lora:wght@400;700&family=Open+Sans:wght@400;600&display=swap">
<style>
:root{
  --red:#8e1f1f;
  --navy:#14234f;
  --ink:#222831;
  --card:#e8e8f8;
  --hero:#6f8a5c;
  --footer:#0a1128;
  --footer-text:#8a9bc4;
  --white:#ffffff;
}
*{margin:0;padding:0;box-sizing:border-box}
h1,h2,h3,h4{font-weight:400}
html,body{width:1200px;height:2364px;overflow:hidden;background:var(--white)}
body{position:relative;font-family:"Open Sans",Arial,sans-serif;color:var(--ink)}
.abs{position:absolute}

.site-header{left:0;top:0;width:1200px;height:81px;background:var(--white)}
.brand{left:144px;top:26px;display:flex;align-items:center;gap:10px}
.brand-dot{width:30px;height:30px;border-radius:50%;background:var(--navy)}
.brand-name{font-family:"Lora",Georgia,serif;font-weight:700;font-size:35px;line-height:1;color:var(--red)}
.nav{top:40px;font-family:"Lora",Georgia,serif;font-size:16px;color:var(--navy);white-space:nowrap}
.nav.active{color:var(--red)}

.shapes{left:0;top:0}
.hero-title{left:0;width:1200px;top:184px;text-align:center;font-family:"Lora",Georgia,serif;font-weight:700;font-size:46px;color:#141414}
.slider-btn{width:40px;height:40px;border-radius:50%;background:var(--white)}

.section-title{left:0;width:1200px;text-align:center;font-family:"Lora",Georgia,serif;font-size:42px;line-height:1.2;color:var(--red)}
.intro{left:140px;width:920px;top:786px;text-align:center;font-size:14.8px;line-height:29px;color:#333}

.offer-card{top:925px;width:440px;height:185px;background:var(--card);border-radius:3px}
.offer-art{left:18px;top:42px;width:96px;height:100px;border-radius:4px}
.offer-title{left:140px;top:18px;font-family:"Lora",Georgia,serif;font-weight:700;font-size:24px;color:var(--navy)}
.offer-text{left:141px;top:54px;width:284px;font-size:12px;line-height:21px;color:#222}
.btn{left:141px;top:125px;width:104px;height:36px;background:var(--navy);color:var(--white);font-family:"Lora",Georgia,serif;font-size:14px;line-height:36px;text-align:center;border-radius:2px}

.future-title{left:0;width:1200px;top:1368px;text-align:center;font-family:"Lora",Georgia,serif;font-size:42px;line-height:1.2;color:var(--white)}
.future-text{left:140px;width:920px;top:1428px;text-align:center;font-size:21px;line-height:37px;color:var(--white)}

.price-card{top:1834px;width:208px;height:119px;background:var(--card);border-radius:2px;text-align:center}
.price-value{position:absolute;left:0;width:208px;top:12px;font-family:"Lora",Georgia,serif;color:var(--navy)}
.price-value b{font-weight:400;font-size:50px}
.price-value span{font-size:17px;margin-left:6px}
.price-rule{position:absolute;left:8px;right:8px;top:74px;height:1px;background:#b9bcd4}
.price-label{position:absolute;left:0;width:208px;top:84px;font-family:"Lora",Georgia,serif;font-size:12px;color:var(--navy)}

.foot-head{top:2162px;font-family:"Lora",Georgia,serif;font-size:20px;color:var(--white)}
.foot-list{top:2196px;font-size:12px;line-height:24px;color:var(--footer-text);list-style:none}
.foot-list li{display:flex;align-items:center;gap:12px}
.foot-list svg{width:10px;height:10px;fill:var(--footer-text)}
.social{top:2202px;width:44px;height:44px;border-radius:50%;border:1px solid #5a6a92}
.foot-rule{left:144px;top:2293px;width:912px;height:1px;background:#2c3656}
.copyright{left:0;width:1200px;top:2321px;text-align:center;font-size:12px;color:var(--footer-text)}
</style>
</head>
<body>

<svg class="abs shapes" width="1200" height="2364" viewBox="0 0 1200 2364">
  <defs>
    <radialGradient id="futureFill" cx=".5" cy=".55" r=".7">
      <stop offset="0" stop-color="#22396a"/>
      <stop offset="1" stop-color="#142454"/>
    </radialGradient>
  </defs>
  <polygon role="img" aria-label="Hero photo: wind turbines on green farmland" fill="var(--hero)" points="0,81 1200,81 1200,656 600,575 600,657 0,575"/>
  <polygon role="img" aria-label="Abstract dark blue data network background" fill="url(#futureFill)" points="0,1198 600,1281 600,1198 1200,1281 1200,1682 600,1600 600,1682 0,1600"/>
  <polygon fill="#0a1128" points="0,2040 600,2123 600,2040 1200,2123 1200,2364 0,2364"/>
</svg>

<header class="abs site-header">
  <div class="abs brand"><span class="brand-dot"></span><span class="brand-name">KVELDBRÁ</span></div>
  <span class="abs nav active" style="left:475px">TERMS OF BUSINESS</span>
  <span class="abs nav" style="left:678px">QUESTION &amp; ANSWER</span>
  <span class="abs nav" style="left:890px">ABOUT KVELDBRÁ</span>
</header>

<h1 class="abs hero-title">SAME ELECTRICITY ~ JUST CHEAPER!</h1>
<div class="abs slider-btn" style="left:56px;top:328px">
  <svg width="40" height="40" viewBox="0 0 40 40"><path d="M23 12 L15 20 L23 28" fill="none" stroke="#14234f" stroke-width="3.5" stroke-linecap="round"/></svg>
</div>
<div class="abs slider-btn" style="left:1103px;top:328px">
  <svg width="40" height="40" viewBox="0 0 40 40"><path d="M17 12 L25 20 L17 28" fill="none" stroke="#14234f" stroke-width="3.5" stroke-linecap="round"/></svg>
</div>

<h2 class="abs section-title" style="top:726px">WELCOME TO KVELDBRÁ</h2>
<p class="abs intro">Kveldbrá is start-up company selling electricity in Iceland. The operations of the company consist of making power usage forecasts for our customers, purchasing the electricity wholesale from the energy producers, and selling the electricity to the consumer. We are focused on tech by using optimization and machine learning to minimize electricity prices to our customers. Our marketing strategy is to portray a tech company mindset and to show dedication to driving down the electricity price on the market.</p>

<div class="abs offer-card" style="left:144px">
  <div class="abs offer-art" role="img" aria-label="Isometric illustration of a house" style="background:linear-gradient(160deg,#c86a92,#a9b6df)"></div>
  <h3 class="abs offer-title">FOR HOME</h3>
  <p class="abs offer-text">Vivamus efficitur ex condimentum, malesuada eros eget, feugiat nibh. Sed tellus imperdiet eget gravida sit amet, volutpat eget turpis.</p>
  <div class="abs btn">READ MORE</div>
</div>
<div class="abs offer-card" style="left:616px">
  <div class="abs offer-art" role="img" aria-label="Isometric illustration of an office tower" style="background:linear-gradient(180deg,#8fa8dc,#5c7cc4)"></div>
  <h3 class="abs offer-title">FOR COMPANY</h3>
  <p class="abs offer-text">Vivamus efficitur ex condimentum, malesuada eros eget, feugiat nibh. Sed tellus imperdiet eget gravida sit amet, volutpat eget turpis.</p>
  <div class="abs btn">READ MORE</div>
</div>

<h2 class="abs future-title">THE FUTURE IS EXCITING</h2>
<p class="abs future-text">Let's make the electricity system smarter together. Kveldbrá uses artificial intelligence, data science and automation to minimize costs and promote eccentricity.</p>

<h2 class="abs section-title" style="top:1760px">PRICE LIST</h2>
<div class="abs price-card" style="left:376px">
  <div class="price-value"><b>6.95</b><span>ISK/kwh</span></div>
  <div class="price-rule"></div>
  <div class="price-label">Vestibulum condimentum</div>
</div>
<div class="abs price-card" style="left:616px">
  <div class="price-value"><b>6.22</b><span>ISK/kwh</span></div>
  <div class="price-rule"></div>
  <div class="price-label">Electric acceleration</div>
</div>

<footer>
  <h4 class="abs foot-head" style="left:144px">Links</h4>
  <ul class="abs foot-list" style="left:144px">
    <li>Terms of Business</li><li>Question &amp; Answer</li><li>About Kveldbrá</li>
  </ul>
  <h4 class="abs foot-head" style="left:360px">Kveldbrá ehf</h4>
  <ul class="abs foot-list" style="left:360px">
    <li>ID number: 510317-0280</li><li>VAT number: 128474</li>
  </ul>
  <h4 class="abs foot-head" style="left:633px">Contact info</h4>
  <ul class="abs foot-list" style="left:633px">
    <li><svg viewBox="0 0 10 10"><path d="M5 0a3.5 3.5 0 0 1 3.5 3.5C8.5 6 5 10 5 10S1.5 6 1.5 3.5A3.5 3.5 0 0 1 5 0zm0 2a1.5 1.5 0 1 0 0 3 1.5 1.5 0 0 0 0-3z"/></svg>Hlíðarvegur 7 200 Kópavogur</li>
    <li><svg viewBox="0 0 10 10"><path d="M0 2h10v6H0z M0 2l5 3.5L10 2" stroke="#0a1128" stroke-width=".8"/></svg>kveldbra@kveldbra.is</li>
    <li><svg viewBox="0 0 10 10"><path d="M2 0l2 2.5-1 1.2c.6 1.3 1.7 2.4 3 3l1.2-1L10 7.8 8.5 10C4 9.6.4 6 0 1.5z"/></svg>555-0142</li>
  </ul>
  <h4 class="abs foot-head" style="left:943px">Follow us on</h4>
  <div class="abs social" style="left:943px"></div>
  <div class="abs social" style="left:999px"></div>
  <div class="abs foot-rule"></div>
  <p class="abs copyright">Copyright © 2021 Kveldbrá. All rights reserved</p>
</footer>

</body>
</html>
```